"Got Radon?" Banner Ads

I need banner ads made for Pelvaro Banner Circuit campaign. There are 10 sizes of banners, so I need all 10 sizes. All of them can be similar in design and concept, but need to look good and the content must fill the space nicely.

The text on the ad is "Got Radon?" big/bold, and there should be a picture of a house with gas seeping into it from the ground. I have attached an example of an existing ad for reference.

These are the 10 sizes of banners that we need:
970x90
120x600
160x600
200x200
250x250
350x250
300x600
336x280
468x60
728x90

```html
<!DOCTYPE html>
<html lang="en">
<head>
<meta charset="utf-8">
<title>Got Radon? Banner Set – Pelvaro Banner Circuit</title>
<link rel="stylesheet" href="https://fonts.googleapis.com/css2?family=Arimo:wght@400;700&family=Oswald:wght@400;500;700&family=Archivo+Black&display=swap">
<style>
:root{
  --green-dark:#0b4d0b;
  --green-mid:#2f6f2f;
  --green-light:#6a9e6a;
  --yellow:#ffec00;
  --white:#ffffff;
  --label:#1f5a1f;
  --page:#ffffff;
  --photo-sky:#c9d6cf;
  --photo-wall:#8f9c8c;
  --photo-brick:#7a5a4a;
  --photo-soil:#6b5a3e;
}
*{margin:0;padding:0;box-sizing:border-box}
html,body{width:952px;height:1200px;overflow:hidden;background:var(--page)}
.sheet{position:relative;width:952px;height:1200px}
.banner{position:absolute;background:var(--green-dark);overflow:hidden;color:var(--white);font-family:"Arimo",Arial,sans-serif}
.size-label{position:absolute;font-family:"Arimo",Arial,sans-serif;font-size:19px;color:var(--label);white-space:nowrap}
.title{color:var(--yellow);font-weight:700;letter-spacing:.04em;white-space:nowrap;line-height:1}
.subtitle{color:var(--white);font-weight:700;letter-spacing:.08em;white-space:nowrap;line-height:1}
.perks{color:var(--white);white-space:nowrap;text-shadow:1px 1px 1px rgba(0,0,0,.6)}
.perks span{display:block}
.cta{font-family:"Archivo Black",sans-serif;color:var(--yellow);white-space:nowrap;line-height:1;
  text-shadow:-1px -1px 0 #000,1px -1px 0 #000,-1px 1px 0 #000,1px 1px 0 #000,2px 2px 2px #000}
.cta-tall{font-family:"Oswald",sans-serif;font-weight:700;color:var(--yellow);line-height:.95;text-align:center;
  text-shadow:-1px -1px 0 #000,1px -1px 0 #000,-1px 1px 0 #000,1px 1px 0 #000}
.tall-title{font-family:"Oswald",sans-serif;font-weight:500;text-align:center}
.perk-band{position:absolute;background:linear-gradient(180deg,var(--green-light),var(--green-mid) 60%,var(--green-dark))}
.perk-band-h{position:absolute;background:linear-gradient(90deg,var(--green-light),var(--green-mid))}
.photo{position:absolute;background:linear-gradient(180deg,var(--photo-sky) 0%,var(--photo-wall) 40%,var(--photo-brick) 70%,var(--photo-soil) 100%)}
.photo-fade{position:absolute;background:linear-gradient(180deg,var(--green-light) 0%,rgba(106,158,106,.6) 25%,var(--photo-wall) 50%,var(--photo-brick) 78%,var(--photo-soil) 100%)}
.abs{position:absolute}
</style>
</head>
<body>
<div class="sheet">

  <!-- 970x90 -->
  <section class="banner" style="left:45px;top:36px;width:776px;height:72px">
    <div class="abs" style="left:11px;top:14px">
      <div class="title" style="font-size:22px">RADON REDUCTION</div>
      <div class="subtitle" style="font-size:12px;margin-top:6px">QUALITY MITIGATION SYSTEMS</div>
    </div>
    <div class="perk-band-h" style="left:250px;top:0;width:177px;height:72px"></div>
    <div class="perks abs" style="left:257px;top:5px;font-size:16px;line-height:21px">
      <span>FREE Estimates</span><span>Same Day Service</span><span>Best Price Guarantee</span>
    </div>
    <div class="photo" role="img" aria-label="Cutaway house with radon gas rising from the ground" style="left:427px;top:0;width:134px;height:72px"></div>
    <div class="cta abs" style="left:571px;top:23px;font-size:24px">GOT RADON?</div>
  </section>
  <div class="size-label" style="left:752px;top:112px">970X90</div>

  <!-- 120x600 -->
  <section class="banner" style="left:44px;top:161px;width:96px;height:480px">
    <div class="tall-title abs" style="left:0;top:14px;width:96px">
      <div style="color:var(--yellow);font-size:19px;line-height:26px">RADON<br>REDUCTION</div>
      <div style="font-size:16px;line-height:27px;margin-top:18px">QUALITY<br>MITIGATION<br>SYSTEMS</div>
    </div>
    <div class="perk-band" style="left:0;top:170px;width:96px;height:104px"></div>
    <div class="perks abs" style="left:6px;top:191px;font-family:'Oswald',sans-serif;font-size:10px;line-height:20px">
      <span>FREE Estimates</span><span>Same Day Service</span><span>Best Price Guarantee</span>
    </div>
    <div class="photo" role="img" aria-label="Cutaway house with radon gas rising from the ground" style="left:0;top:274px;width:96px;height:87px"></div>
    <div class="cta-tall abs" style="left:0;top:380px;width:96px">
      <div style="font-size:44px">GOT</div><div style="font-size:22px">RADON?</div>
    </div>
  </section>
  <div class="size-label" style="left:62px;top:645px">120X600</div>

  <!-- 160x600 -->
  <section class="banner" style="left:210px;top:162px;width:128px;height:480px">
    <div class="tall-title abs" style="left:0;top:18px;width:128px">
      <div style="color:var(--yellow);font-size:24px;line-height:31px">RADON<br>REDUCTION</div>
      <div style="font-size:18px;line-height:23px;margin-top:14px;letter-spacing:.05em">QUALITY<br>MITIGATION<br>SYSTEMS</div>
    </div>
    <div class="perk-band" style="left:0;top:169px;width:128px;height:104px"></div>
    <div class="perks abs" style="left:8px;top:178px;font-family:'Oswald',sans-serif;font-size:13px;line-height:20px">
      <span>FREE Estimates</span><span>Same Day Service</span><span>Best Price Guarantee</span>
    </div>
    <div class="photo" role="img" aria-label="Cutaway house with radon gas rising from the ground" style="left:0;top:273px;width:128px;height:95px"></div>
    <div class="cta-tall abs" style="left:0;top:382px;width:128px">
      <div style="font-size:52px">GOT</div><div style="font-size:27px">RADON?</div>
    </div>
  </section>
  <div class="size-label" style="left:260px;top:647px">160X600</div>

  <!-- 200x200 -->
  <section class="banner" style="left:397px;top:162px;width:160px;height:160px">
    <div class="abs" style="left:7px;top:3px">
      <div class="title" style="font-size:13px">RADON REDUCTION</div>
      <div class="subtitle" style="font-size:8px;letter-spacing:.03em;margin-top:3px">QUALITY MITIGATION SYSTEMS</div>
    </div>
    <div class="photo-fade" role="img" aria-label="Cutaway house with radon gas rising from the ground" style="left:0;top:30px;width:160px;height:130px"></div>
    <div class="perks abs" style="left:7px;top:32px;font-size:9px;line-height:11px">
      <span>FREE Estimates</span><span>Same Day Service</span><span>Best Price Guarantee</span>
    </div>
    <div class="cta abs" style="left:10px;top:135px;font-size:17px">GOT RADON?</div>
  </section>
  <div class="size-label" style="left:478px;top:326px">200X200</div>

  <!-- 250x250 -->
  <section class="banner" style="left:619px;top:162px;width:200px;height:200px">
    <div class="abs" style="left:9px;top:4px">
      <div class="title" style="font-size:17px">RADON REDUCTION</div>
      <div class="subtitle" style="font-size:10px;margin-top:4px;font-weight:400">QUALITY MITIGATION SYSTEMS</div>
    </div>
    <div class="photo-fade" role="img" aria-label="Cutaway house with radon gas rising from the ground" style="left:0;top:38px;width:200px;height:162px"></div>
    <div class="perks abs" style="left:9px;top:40px;font-size:11px;line-height:13.5px">
      <span>FREE Estimates</span><span>Same Day Service</span><span>Best Price Guarantee</span>
    </div>
    <div class="cta abs" style="left:13px;top:169px;font-size:22px">GOT RADON?</div>
  </section>
  <div class="size-label" style="left:738px;top:364px">250X250</div>

  <!-- 350x250 -->
  <section class="banner" style="left:390px;top:402px;width:280px;height:200px">
    <div class="abs" style="left:16px;top:6px">
      <div class="title" style="font-size:22px">RADON REDUCTION</div>
      <div class="subtitle" style="font-size:12px;margin-top:5px;font-weight:400">QUALITY MITIGATION SYSTEMS</div>
    </div>
    <div class="photo-fade" role="img" aria-label="Cutaway house with radon gas rising from the ground" style="left:0;top:47px;width:280px;height:153px"></div>
    <div class="perks abs" style="left:15px;top:51px;font-size:11px;line-height:14px">
      <span>FREE Estimates</span><span>Same Day Service</span><span>Best Price Guarantee</span>
    </div>
    <div class="cta abs" style="left:16px;top:166px;font-size:22px">GOT RADON?</div>
  </section>
  <div class="size-label" style="left:590px;top:602px">350X250</div>

  <!-- 300x600 -->
  <section class="banner" style="left:44px;top:686px;width:240px;height:480px">
    <div class="abs" style="left:0;top:10px;width:240px;text-align:center">
      <div class="title" style="font-size:30px;line-height:31px">RADON<br>REDUCTION</div>
      <div class="subtitle" style="font-size:21px;line-height:24.5px;margin-top:10px">QUALITY<br>MITIGATION<br>SYSTEMS</div>
    </div>
    <div class="perk-band" style="left:0;top:163px;width:240px;height:85px"></div>
    <div class="perks abs" style="left:10px;top:170px;font-size:18px;line-height:24.5px">
      <span>FREE Estimates</span><span>Same Day Service</span><span>Best Price Guarantee</span>
    </div>
    <div class="photo" role="img" aria-label="Cutaway house with radon gas rising from the ground" style="left:0;top:248px;width:240px;height:172px"></div>
    <div class="cta-tall abs" style="left:0;top:424px;width:240px;font-size:43px;line-height:48px">GOT RADON?</div>
  </section>
  <div class="size-label" style="left:207px;top:1173px">300X600</div>

  <!-- 336x280 -->
  <section class="banner" style="left:383px;top:683px;width:269px;height:224px">
    <div class="abs" style="left:15px;top:6px">
      <div class="title" style="font-size:23px">RADON REDUCTION</div>
      <div class="subtitle" style="font-size:13px;margin-top:3px;font-weight:400">QUALITY MITIGATION SYSTEMS</div>
    </div>
    <div class="photo-fade" role="img" aria-label="Cutaway house with radon gas rising from the ground" style="left:0;top:48px;width:269px;height:176px"></div>
    <div class="perks abs" style="left:14px;top:52px;font-size:12px;line-height:13.5px">
      <span>FREE Estimates</span><span>Same Day Service</span><span>Best Price Guarantee</span>
    </div>
    <div class="cta abs" style="left:27px;top:193px;font-size:25px">GOT RADON?</div>
  </section>
  <div class="size-label" style="left:573px;top:919px">336X280</div>

  <!-- 468x60 -->
  <section class="banner" style="left:381px;top:971px;width:374px;height:48px">
    <div class="abs" style="left:7px;top:8px">
      <div class="title" style="font-family:'Oswald',sans-serif;font-weight:500;font-size:18px;letter-spacing:0">RADON REDUCTION</div>
      <div class="subtitle" style="font-family:'Oswald',sans-serif;font-weight:400;font-size:10px;letter-spacing:.02em;margin-top:3px">QUALITY MITIGATION SYSTEMS</div>
    </div>
    <div class="photo" role="img" aria-label="Cutaway house with radon gas rising from the ground" style="left:159px;top:0;width:90px;height:48px"></div>
    <div class="perk-band-h" style="left:249px;top:0;width:125px;height:28px;background:linear-gradient(90deg,var(--green-mid),var(--green-dark))"></div>
    <div class="perks abs" style="left:253px;top:2px;font-size:7px;line-height:8px;font-weight:700">
      <span>FREE Estimates</span><span>Same Day Service</span><span>Best Price Guarantee</span>
    </div>
    <div class="cta abs" style="left:253px;top:30px;font-size:14px">GOT RADON?</div>
  </section>
  <div class="size-label" style="left:690px;top:1035px">468X60</div>

  <!-- 728x90 -->
  <section class="banner" style="left:333px;top:1090px;width:582px;height:72px">
    <div class="abs" style="left:11px;top:10px">
      <div class="title" style="font-family:'Oswald',sans-serif;font-weight:500;font-size:26px;letter-spacing:0">RADON REDUCTION</div>
      <div class="subtitle" style="font-family:'Oswald',sans-serif;font-weight:400;font-size:14.5px;letter-spacing:.03em;margin-top:5px">QUALITY MITIGATION SYSTEMS</div>
    </div>
    <div class="photo" role="img" aria-label="Cutaway house with radon gas rising from the ground" style="left:246px;top:0;width:143px;height:72px"></div>
    <div class="perk-band-h" style="left:389px;top:0;width:193px;height:42px;background:linear-gradient(90deg,var(--green-mid),var(--green-dark))"></div>
    <div class="perks abs" style="left:394px;top:2px;font-size:11px;line-height:12.5px;font-weight:700">
      <span>FREE Estimates</span><span>Same Day Service</span><span>Best Price Guarantee</span>
    </div>
    <div class="cta abs" style="left:394px;top:45px;font-size:22px">GOT RADON?</div>
  </section>
  <div class="size-label" style="left:848px;top:1168px">728X90</div>

</div>
</body>
</html>
```